Yacht, Boats, Watersports company needs a redesign of business card

Hello Designers!
We are a Boat dealership company that sells fun in the water, we sell boats, Yachts, Kayaks and also yacht WaterSport toys. We are looking to redesign our business cards in to something a little bit more sophisticated. in a way that we can make better use of our company colors. I'm attaching a zipped file containing the company 3 sets of company logo which one is an horizontal another one is a vertical and also a chromed 3d logo. Also is included two set of business cards that we use and also some designs that i think it's interesting. We use PMS 2026c Orange and PMS 7687C Blue. I would like to see at least two different options with the orange as accent and also using blue as an accent color. It's really important for the business cards to have a font option and size that is legible to most people. Our current website is wwww.corvellamarine.com. Please visit if you want to have a better feeling of the Boat dealership
You can send Single sided or double side options. We are now using single sided but we may be open for a double side option if we really like the design.
Target Market(s)
Marine, boat sales, yacht sales, water toys sales/
Contact Information for Business Card
Name: Dale Pritchett
Address: 718 West Halden Lane,
Dania Beach, FL 33019
Phone: 954-382-7146
Fax: 954:382-7139
Cell: 954-451-8320
Email: 212@corvellamarine.com
Website: corvellamarine.com
Requirements
Must have
- the current information of the business card provided.
logo
use the PMS Colors
Nice to have
- a touch of elegance and sophistication but simple
Should not have
- should not have any typography that is hard to read, the card should be simple but yet sophisticated.

```html
<!DOCTYPE html>
<html lang="en">
<head>
<meta charset="UTF-8">
<title>Corvella Marine – Business Card</title>
<link rel="stylesheet" href="https://fonts.googleapis.com/css2?family=Montserrat:wght@500;600;700;800&display=swap">
<style>
  :root {
    --orange: #e8532a;
    --blue: #1f3c8c;
    --blue-light: #3a5bb8;
    --yellow: #f7c21c;
    --amber: #f29433;
    --paper: #ffffff;
    --backdrop: #efebe4;
    --card-w: 540px;
    --card-h: 310px;
  }
  * { box-sizing: border-box; margin: 0; padding: 0; }
  html, body { width: 1200px; height: 750px; overflow: hidden; }
  body {
    background: var(--backdrop);
    font-family: "Montserrat", sans-serif;
    position: relative;
  }
  .card {
    position: absolute;
    top: 220px;
    width: var(--card-w);
    height: var(--card-h);
    background: var(--paper);
    box-shadow: 0 12px 30px rgba(60, 40, 20, 0.18);
    overflow: hidden;
  }
  .card--front { left: 40px; }
  .card--back { left: 620px; }
  .card__art { position: absolute; inset: 0; width: 100%; height: 100%; }

  .brand {
    display: flex;
    align-items: center;
    gap: 10px;
    position: relative;
  }
  .brand__dot {
    border-radius: 50%;
    border: 4px solid var(--orange);
    flex: none;
  }
  .brand__name {
    font-weight: 800;
    color: var(--blue);
    text-transform: uppercase;
    letter-spacing: 0.08em;
  }

  /* front */
  .front__content {
    position: absolute;
    inset: 0;
    display: flex;
    flex-direction: column;
    align-items: center;
    justify-content: center;
    gap: 14px;
  }
  .card--front .brand { flex-direction: column; gap: 12px; }
  .card--front .brand__dot { width: 62px; height: 62px; border-width: 5px; }
  .card--front .brand__name { font-size: 28px; }
  .front__web {
    font-size: 14px;
    font-weight: 500;
    color: var(--blue);
    letter-spacing: 0.03em;
    position: relative;
  }

  /* back */
  .back__content { position: absolute; left: 28px; top: 24px; right: 28px; }
  .card--back .brand__dot { width: 36px; height: 36px; }
  .card--back .brand__name { font-size: 15px; }
  .holder {
    margin-top: 18px;
    font-size: 30px;
    font-weight: 700;
    color: var(--blue);
  }
  .holder__rule {
    width: 270px;
    height: 2px;
    background: var(--orange);
    margin-top: 6px;
  }
  .contact { list-style: none; margin-top: 12px; }
  .contact__item {
    display: flex;
    align-items: flex-start;
    gap: 10px;
    font-size: 13px;
    font-weight: 600;
    color: var(--blue);
    letter-spacing: 0.06em;
    line-height: 1.45;
  }
  .contact__icon { width: 13px; height: 13px; margin-top: 3px; flex: none; fill: var(--orange); }
</style>
</head>
<body>

<section class="card card--front" aria-label="Card front">
  <svg class="card__art" viewBox="0 0 540 310" aria-hidden="true">
    <defs>
      <linearGradient id="front-warm" x1="0" y1="0" x2="1" y2="1">
        <stop offset="0" stop-color="#f7c21c"/>
        <stop offset="1" stop-color="#f29433"/>
      </linearGradient>
      <linearGradient id="front-cool" x1="0" y1="0" x2="1" y2="1">
        <stop offset="0" stop-color="#3a5bb8"/>
        <stop offset="1" stop-color="#1f3c8c"/>
      </linearGradient>
    </defs>
    <path d="M470,0 L540,0 L540,110 L505,100 Q475,92 468,65 L462,30 Q460,10 470,0 Z" fill="url(#front-warm)"/>
    <path d="M505,110 L540,118 L540,240 L512,232 Q492,226 488,205 L480,160 Q476,120 505,110 Z" fill="url(#front-cool)"/>
    <path d="M0,180 L42,190 Q68,198 64,225 L56,272 L0,262 Z" fill="url(#front-cool)"/>
    <path d="M0,258 L150,268 Q175,270 195,284 L230,310 L0,310 Z" fill="url(#front-warm)"/>
  </svg>
  <div class="front__content">
    <div class="brand">
      <span class="brand__dot"></span>
      <span class="brand__name">Corvella Marine</span>
    </div>
    <p class="front__web">corvellamarine.com</p>
  </div>
</section>

<section class="card card--back" aria-label="Card back">
  <svg class="card__art" viewBox="0 0 540 310" aria-hidden="true">
    <defs>
      <linearGradient id="back-warm" x1="0" y1="0" x2="1" y2="0">
        <stop offset="0" stop-color="#f7b21c"/>
        <stop offset="1" stop-color="#f29433"/>
      </linearGradient>
      <linearGradient id="back-yellow" x1="0" y1="0" x2="1" y2="1">
        <stop offset="0" stop-color="#f7c21c"/>
        <stop offset="1" stop-color="#f4a022"/>
      </linearGradient>
      <linearGradient id="back-cool" x1="0" y1="0" x2="1" y2="1">
        <stop offset="0" stop-color="#3a5bb8"/>
        <stop offset="1" stop-color="#1f3c8c"/>
      </linearGradient>
    </defs>
    <path d="M330,0 L430,0 L408,42 Q398,58 378,52 L330,36 Z" fill="url(#back-cool)"/>
    <path d="M420,0 L540,0 L540,10 L510,62 Q500,76 480,70 L405,44 Z" fill="url(#back-yellow)"/>
    <path d="M455,212 Q462,178 495,182 L540,190 L540,240 L455,240 Z" fill="url(#back-cool)"/>
    <path d="M0,290 L340,238 Q362,234 380,236 L540,224 L540,310 L0,310 Z" fill="url(#back-warm)"/>
  </svg>
  <div class="back__content">
    <div class="brand">
      <span class="brand__dot"></span>
      <span class="brand__name">Corvella Marine</span>
    </div>
    <h1 class="holder">Dale Pritchett</h1>
    <div class="holder__rule"></div>
    <ul class="contact">
      <li class="contact__item">
        <svg class="contact__icon" viewBox="0 0 16 16" aria-hidden="true"><path d="M3.5 1 L6 1 L7 5 L5.3 6.3 Q6.5 9 9.7 10.7 L11 9 L15 10 L15 12.5 Q15 15 12.5 15 Q1 14 1 3.5 Q1 1 3.5 1 Z"/></svg>
        <span>555-382-7146</span>
      </li>
      <li class="contact__item">
        <svg class="contact__icon" viewBox="0 0 16 16" aria-hidden="true"><path d="M4 1 H12 V5 H4 Z M1 6 H15 V12 H12 V10 H4 V12 H1 Z M5 11 H11 V15 H5 Z"/></svg>
        <span>555:382-7139</span>
      </li>
      <li class="contact__item">
        <svg class="contact__icon" viewBox="0 0 16 16" aria-hidden="true"><path d="M1 3 H15 V13 H1 Z M2 4 L8 9 L14 4 Z" fill-rule="evenodd"/></svg>
        <span>555-451-8320</span>
      </li>
      <li class="contact__item">
        <svg class="contact__icon" viewBox="0 0 16 16" aria-hidden="true"><path d="M8 1 Q13 1 13 6 Q13 10 8 15 Q3 10 3 6 Q3 1 8 1 Z M8 4 A2 2 0 1 0 8 8 A2 2 0 1 0 8 4 Z" fill-rule="evenodd"/></svg>
        <span>718 West Halden Lane,<br>Port Merrow, GA 33019</span>
      </li>
    </ul>
  </div>
</section>

</body>
</html>
```